Maple Hollow Canine Massage Needs a Business Card Design

Maple Hollow Canine Massage is a new therapeutic canine massage company located in Nederland, Colorado. I need a business card design that include my logo and basic contact information.

Target Market(s)

Pet owners, veterinarians

Industry/Entity Type

Business

Contact Information for Business Card

Lydia Ferrow, CCMT
303.518.7269
lydia@maplehollowmassage.example
www.maplehollowmassage.example

Colors
6c459b
886aae
b8a6cd
a64599
b768aa
d3a5cc
fbed22

Requirements
Must have
• Font should be similar to font in logo.

```html
<!DOCTYPE html>
<html lang="en">
<head>
<meta charset="utf-8">
<title>Maple Hollow Canine Massage – Business Card</title>
<link rel="stylesheet" href="https://fonts.googleapis.com/css2?family=Lato:wght@400;700&display=swap">
<style>
  :root {
    --backdrop: #2a2a2c;
    --card-white: #f4f4f4;
    --plum: #3d1d45;
    --plum-deep: #321638;
    --violet-soft: #9a75b5;
    --gold: #e2b625;
    --silver: #c9c9cc;
  }
  * { box-sizing: border-box; margin: 0; padding: 0; }
  html, body {
    width: 1200px; height: 873px; overflow: hidden;
    background: var(--backdrop);
    font-family: "Lato", sans-serif;
  }
  .card {
    position: absolute; left: 180px; top: 196px;
    width: 840px; height: 480px;
    border-radius: 26px; overflow: hidden;
    background: var(--card-white);
    box-shadow: 0 18px 40px rgba(0,0,0,.5);
  }
  .card-shape { position: absolute; inset: 0; }
  .brand {
    position: absolute; left: 240px; top: 30px;
    width: 220px; height: 220px; border-radius: 50%;
    background: var(--violet-soft);
    display: flex; align-items: center; justify-content: center;
    text-align: center; padding: 30px;
  }
  .brand-name {
    color: var(--gold); font-weight: 700;
    font-size: 25px; line-height: 1.15; letter-spacing: .5px;
  }
  .person {
    position: absolute; right: 60px; top: 232px; text-align: right;
  }
  .person-name { color: var(--silver); font-weight: 700; font-size: 26px; }
  .person-role { color: var(--gold); font-size: 17px; margin-top: 4px; }
  .contact {
    position: absolute; left: 52px; bottom: 46px;
    list-style: none; color: var(--silver); font-size: 16px;
  }
  .contact li { display: flex; align-items: center; gap: 14px; margin-top: 12px; }
  .contact svg { width: 20px; height: 16px; fill: var(--silver); }
  .contact .web { color: var(--gold); font-weight: 700; font-size: 18px; }
</style>
</head>
<body>
  <div class="card">
    <svg class="card-shape" viewBox="0 0 840 480" width="840" height="480" aria-hidden="true">
      <defs>
        <linearGradient id="plumFill" x1="0" y1="0" x2="0" y2="1">
          <stop offset="0" stop-color="#3f1e48"/>
          <stop offset="1" stop-color="#331739"/>
        </linearGradient>
      </defs>
      <path d="M0 318 Q 330 120 840 96 L840 480 L0 480 Z" fill="url(#plumFill)"/>
      <path d="M0 306 Q 330 108 840 84" fill="none" stroke="var(--gold)" stroke-width="3"/>
    </svg>

    <div class="brand">
      <span class="brand-name">Maple Hollow Canine Massage</span>
    </div>

    <div class="person">
      <div class="person-name">Lydia Ferrow</div>
      <div class="person-role">Owner/ Founder</div>
    </div>

    <ul class="contact">
      <li>
        <svg viewBox="0 0 20 16"><path d="M1 5c0-2 4-4 9-4s9 2 9 4v2h-4V5c-2-.6-8-.6-10 0v2H1z"/><path d="M5 8h10l3 7H2z"/></svg>
        <span>303.518.7269</span>
      </li>
      <li>
        <svg viewBox="0 0 20 16"><path d="M1 2h18v12H1z M2.5 3.5 10 9l7.5-5.5v-.1H2.5z" fill-rule="evenodd"/></svg>
        <span>lydia@maplehollowmassage.example</span>
      </li>
      <li class="web">www.maplehollowmassage.example</li>
    </ul>
  </div>
</body>
</html>
```